Sports hypnotherapist needs electronic letterhead design

Need a simple but classy design for a letterhead that looks good when printed. Its for a hypnotherapist who specialises in elite sport. Should have my company name and address and website details on it. I specialise in footballers.
Should look good electronically and when printed.
Include all contact details as shown in the must haves.

Target Market(s)

Sports people, elite sport.

Industry/Entity Type

Hypnotherapy

Font styles to use
Sans Serif

Colors

Designer to choose colors to be used in the design.

Requirements
Must have
• NEEDS TO BE DESIGNED IN MS WORD
• Logo +
• Tidewell Path Hypnotherapists
• 27 Marlowby Close
• Bracknell
• RG14 3TX
• Tel: 07814 265173
• E: tidewellcoaching@brookmail.example
• www: http://www.tidewell-path.example.
• Colin Dearsley
• Clinical hypnotherapist, hypnoanalyst, mental resilience coach, MSc, Dip PHH
Nice to have
• A watermark?
• Plenty of space for the A4 letter
• Prints well.
Should not have
• Too much clutter.
• Too much colour that will be costly to print.

```html
<!DOCTYPE html>
<html lang="en">
<head>
<meta charset="utf-8">
<title>Tidewell Path Hypnotherapists – Letterhead</title>
<link href="https://fonts.googleapis.com/css2?family=Roboto:wght@400;500;700&display=swap" rel="stylesheet">
<style>
  :root {
    --backdrop: #e6e6e8;
    --paper: #fbfbfd;
    --ink: #1d1d1f;
    --ink-soft: #3c3c44;
    --ink-muted: #55555c;
    --accent: #2ea3dc;
    --mark-grey: #9a9aa6;
    --mark-blue: #b9d8ee;
  }
  * { box-sizing: border-box; margin: 0; padding: 0; }
  html, body {
    width: 1085px; height: 1200px; overflow: hidden;
    background: var(--backdrop);
    font-family: "Roboto", Arial, sans-serif;
    color: var(--ink);
  }
  .letterhead {
    position: absolute; left: 118px; top: 0;
    width: 849px; height: 1200px;
    background: var(--paper);
  }
  .brand {
    position: absolute; left: 44px; top: 64px;
    display: flex; align-items: center; gap: 12px;
  }
  .brand-dot { width: 34px; height: 34px; border-radius: 50%; background: var(--accent); }
  .brand-name { font-size: 33px; font-weight: 700; color: var(--ink); letter-spacing: -0.3px; }
  .practitioner {
    position: absolute; right: 34px; top: 64px; text-align: right;
  }
  .practitioner-name { font-size: 23px; font-weight: 500; letter-spacing: 1.5px; }
  .practitioner-title { font-size: 16px; color: var(--ink-soft); line-height: 20px; margin-top: 8px; letter-spacing: 0.3px; }
  .recipient { position: absolute; left: 52px; top: 202px; }
  .recipient-label { font-size: 16px; color: var(--ink-soft); }
  .recipient-name { font-size: 18px; font-weight: 500; }
  .recipient-role { font-size: 13px; font-weight: 500; }
  .letter-body {
    position: absolute; left: 52px; top: 276px; width: 750px;
    font-size: 14px; line-height: 23px; color: var(--ink-soft); text-align: justify;
  }
  .letter-body p + p { margin-top: 21px; }
  .signature { position: absolute; left: 66px; top: 845px; }
  .signature-hand { width: 230px; height: 60px; background: linear-gradient(90deg, #d8d8de, #ececf0); border-radius: 4px; }
  .signature-rule { width: 220px; height: 1px; background: #b8b8c0; margin-top: 8px; }
  .signature-role { font-size: 16px; color: var(--ink-muted); margin: 6px 0 0 38px; }
  .watermark {
    position: absolute; left: 700px; top: 790px; width: 136px; height: 355px;
    background: linear-gradient(160deg, var(--mark-blue), var(--mark-grey));
    opacity: 0.75; border-radius: 60px 60px 8px 8px;
  }
  .footer-rule { position: absolute; left: 32px; top: 1055px; width: 625px; height: 2px; background: var(--accent); }
  .footer {
    position: absolute; left: 32px; top: 1078px; width: 650px;
    display: flex; font-size: 14px; line-height: 18px; color: var(--ink-soft); letter-spacing: 0.4px;
  }
  .footer-address { width: 185px; }
  .footer-online { width: 300px; }
  .footer-label { font-weight: 700; color: var(--ink); }
  .footer-link { color: var(--accent); }
</style>
</head>
<body>
  <main class="letterhead">
    <div class="brand">
      <span class="brand-dot"></span>
      <span class="brand-name">Tidewell Path</span>
    </div>

    <div class="practitioner">
      <div class="practitioner-name">COLIN DEARSLEY</div>
      <div class="practitioner-title">Clinical hypnotherapist, hypnoanalyst,<br>Mental Resilience Coach, MSc, Dip PHH</div>
    </div>

    <div class="recipient">
      <div class="recipient-label">To</div>
      <div class="recipient-name">Martin Greaves, <span class="recipient-role">CEO, NORTHFIELD STUDIO</span></div>
    </div>

    <div class="letter-body">
      <p>Lorem ipsum dolor sit amet, an habeo errem euismod pri. Per id tation exerci lucilius. Usu at congue interesset, est explicari moderatius et, id pro esse docendi. Mea ancillae mentitum atomorum ne, eum congue ponderum eu. Ut mei quidam detraxit similique, dissentias omittantur ut mei.</p>
      <p>Cu nec purto accusam, aliquid graecis disputando quo cu, id augue affert nam. Ex quo cibo iuvaret explicari. In postea disputationi mea, meliore recusabo hendrerit ius et, alienum molestie torquatos vel et. Nam virtute recteque inciderint ei. Sed clita similique quaerendum ut, ex dolorem constituto eos, cu elit elitr ancillae eos. Virtute mentitum invidunt mea te. Qui quis tollit disputando cu, modus melius ne mel.</p>
      <p>Duo oportere petentium in, odio putant placerat usu ad. Vis ut error electram, id placerat singulis postulant his, pri graecis accommodare at. Ut qui ignota inermis partiendo, vis maiestatis abhorreant ei, cu utinam posidonium eam. Mel odio nibh delenit ei, vel ad quodsi impetus explicari. Te mea facilis recteque, harum munere nostrud ea usu. Alii meis est ne, eos consul mucius forensibus te.</p>
      <p>Cu nec purto accusam, aliquid graecis disputando quo cu, id augue affert nam. Ex quo cibo iuvaret explicari. In postea disputationi mea, meliore recusabo hendrerit ius et, alienum molestie torquatos vel et. Nam virtute recteque inciderint ei. Sed clita similique quaerendum ut, ex dolorem constituto eos, cu elit elitr ancillae eos. Virtute mentitum invidunt mea te. Qui quis tollit disputando cu, modus melius ne mel.</p>
      <p>Lorem ipsum dolor sit amet, an habeo errem euismod pri. Per id tation exerci lucilius. Usu at congue interesset, est explicari moderatius et, id pro esse docendi. Mea ancillae mentitum atomorum ne, eum congue ponderum eu. Ut</p>
    </div>

    <div class="signature">
      <div class="signature-hand" role="img" aria-label="Handwritten signature of Colin Dearsley"></div>
      <div class="signature-rule"></div>
      <div class="signature-role">your designation</div>
    </div>

    <div class="watermark" role="img" aria-label="Faint watermark of the practice's standing-figure emblem"></div>

    <div class="footer-rule"></div>
    <div class="footer">
      <div class="footer-address">27 Marlowby Close<br>Bracknell, RG14 3TX</div>
      <div class="footer-online">
        <span class="footer-label">Email:</span> <span class="footer-link">tidewellcoaching@brookmail.example</span><br>
        <span class="footer-label">Web:</span> <span class="footer-link">http://www.tidewell-path.example</span>
      </div>
      <div class="footer-phone"><span class="footer-label">Tel:</span> <span class="footer-link">07814 265173</span></div>
    </div>
  </main>
</body>
</html>
```